Commercial Web Site for software product

Ledgerly is a GDPR compliant Membership, Contact Management & List Management solution. It is an ideal replacement for any organisation or company still using Sheetwise, Mailpost, simple database or paper-based system to manage contact data, mail lists, and other personal information.
The target market will be Clubs/Associations in the EU.
The design will need to be a fluid design and suitable for mobile devices. The home page will contain most of the web site content, enabling a user to scroll through all the relevant information on one page. There will be a single sub page design required for supporting information.
The web site will need to support two language versions - English and German (Language selection option required). However, the build requirements will be for a static HTML site (no database) in English only. We will duplicate and make the German version ourselves.
The attached document is the first draft of the home page content. Whilst it is a little wordy, it should convey the main information that we wish to get across.
Please note: We would prefer not to use photographs for the main imagery, we feel vector graphics would be a better option . As a guide, the following design: https://en.pixelvane.example/profiles/Marlowe/designs/5502147 may provide an insight into how we imagine the home page working and contains all the key elements we would expect to be covered.
The logo contained in the attached document can be split into a logo and text. Feel free to use only the logo (without text) or separate and place the text alongside etc., We do not want to change the logo, however, how you chose to use it is up to you.
Colour's are also optional. We like the blue, but are open to alternative ideas.
The testimonials section, should contain all the questions (3) and several of the associated answers shown. Questions/Answers may be separated into speech bubbles or similar. Not all answers will be used, but are there to provide some content.
The sub pages will be used to provide background on the GDPR requirements, our Service Offering, About Us (possibly), and a contact page.
Updates
The design budget is now guaranteed.
Whilst we have no intention not to move forward with this project, I understand the 'lack of commitment' from our side may be a negative.
Once we have reviewed all submissions - we will decide upon our preferred submission.
We will only request changes from one or two designers, and will make it clear how many other designers are in the running. This I believe is fair, as you probably need this information before deciding whether to submit any changes requested!
My hope is we have a home page that enables a visitor to clearly understand what we are offering, without having to drill down into various sub pages or sections to understand the basics. I appreciate we need to write appropriate content, but the design itself should feel uncluttered and fluid.
Hopefully some of you really talented designers can throw some ideas into the pot. The concept is more important than the detail.
Thanks for considering this project.
Coding
Number of Pages Required
Font styles to use
Colors
Look and feel

```html
<!DOCTYPE html>
<html lang="en">
<head>
<meta charset="utf-8">
<title>Ledgerly – GDPR compliant membership &amp; contact management</title>
<link href="https://fonts.googleapis.com/css2?family=Raleway:wght@500;600;700;800&family=Lato:wght@400;700&display=swap" rel="stylesheet">
<style>
  :root{
    --blue:#0a53d6;
    --band:#0556d8;
    --sky:#a8c7f4;
    --ink:#111318;
    --muted:#7b7f86;
    --body:#3a3d42;
    --card:#ffffff;
    --field:#fafbfc;
    --foot:#f5f5f6;
    --grey-chev:#9a9da3;
    --tick:#27b34a;
  }
  *{box-sizing:border-box;margin:0;padding:0}
  html,body{width:1200px;height:4399px;overflow:hidden;background:#fff}
  body{position:relative;font-family:"Lato",sans-serif;color:var(--body)}
  .abs{position:absolute}
  h1,h2,h3{font-family:"Raleway",sans-serif;color:var(--ink)}
  a{color:inherit;text-decoration:none}

  .hero-bg{position:absolute;left:0;top:0;width:1200px;height:680px}
  .brand{left:112px;top:34px;font-weight:700;font-size:26px;color:#fff;display:flex;align-items:center;gap:10px}
  .brand .dot{width:22px;height:22px;border-radius:50%;background:#fff}
  .nav{top:38px;left:580px;font-size:13px;color:#1d2233}
  .nav a{position:absolute;white-space:nowrap}
  .nav .login{color:var(--blue);font-weight:700}
  .lang{left:1021px;top:34px;width:66px;height:28px;border:1.5px solid var(--blue);border-radius:14px;font-size:11px;color:var(--blue);font-weight:700;display:flex;align-items:center;justify-content:center;gap:6px}
  .hero-title{left:112px;top:176px;font-size:57px;line-height:62px;font-weight:800;letter-spacing:.5px}
  .hero-text{left:112px;top:314px;width:400px;font-size:13px;line-height:22px;color:#222}
  .btn{display:flex;align-items:center;justify-content:center;gap:10px;background:var(--blue);color:#fff;font-weight:700;font-size:13px;border-radius:20px}
  .hero-art{left:525px;top:75px;width:670px;height:440px;border-radius:24px;background:linear-gradient(135deg,#cfe0fa,#7fa6ea 60%,#3b64b8)}

  .section-title{font-size:33px;font-weight:600}
  .copy{font-size:14px;line-height:28px;color:var(--muted)}
  .art{border-radius:18px}

  .feature-list{list-style:none;font-size:14.5px;color:var(--muted)}
  .feature-list li{position:relative;padding-left:21px;height:28.3px;line-height:28.3px;white-space:nowrap}
  .feature-list li::before{content:"";position:absolute;left:0;top:9px;width:11px;height:11px;border-radius:50%;background:var(--blue)}
  .feature-list li::after{content:"";position:absolute;left:2.5px;top:12.5px;width:3px;height:3px;border-top:1.5px solid #fff;border-right:1.5px solid #fff;transform:rotate(45deg)}

  .band{left:0;top:2034px;width:1200px;height:322px;background:var(--band)}
  .card{background:var(--card);border-radius:16px;box-shadow:0 14px 40px rgba(20,40,90,.12);text-align:center}
  .card h3{font-size:24px;line-height:43px;font-weight:600}
  .card p{font-size:14px;line-height:26.5px;color:#2c2f35}
  .card .more{color:var(--blue);font-weight:700;font-size:14px}

  .centered{left:0;width:1200px;text-align:center}
  .q{font-family:"Raleway",sans-serif;font-weight:700;font-size:16px;line-height:26.5px;color:var(--ink)}
  .q .num{color:var(--blue)}
  .q-ico{position:absolute;width:13px;height:13px;border-radius:50%;background:var(--blue);color:#fff;font-size:9px;font-weight:700;text-align:center;line-height:13px}
  .chev{position:absolute;width:26px;height:26px;border-radius:50%}
  .chev::after{content:"";position:absolute;left:9px;width:7px;height:7px;border-right:2px solid #fff;border-bottom:2px solid #fff}
  .chev.down{background:var(--blue)}
  .chev.down::after{top:6px;transform:rotate(45deg)}
  .chev.up{background:var(--grey-chev)}
  .chev.up::after{top:10px;transform:rotate(-135deg)}
  .answers{list-style:none;font-size:13px;line-height:26.6px;color:#333}
  .answers li{position:relative;padding-left:12px}
  .answers li::before{content:"";position:absolute;left:-9px;top:9px;width:9px;height:9px;border-radius:50%;background:var(--tick)}
  .qcard{background:#fff;box-shadow:0 8px 28px rgba(0,0,0,.09)}

  .c-ico{width:50px;height:50px;border-radius:50%;border:2px solid var(--blue);display:flex;align-items:center;justify-content:center}
  .c-title{font-family:"Raleway",sans-serif;font-weight:700;font-size:20px;color:var(--ink)}
  .c-text{font-size:14px;line-height:24px;color:#222}
  .field{background:var(--field);box-shadow:0 4px 14px rgba(0,0,0,.05);font-size:14px;color:#8a8d92;padding:14px 24px}
  .submit{background:var(--blue);color:#fff;font-weight:700;font-size:18px;display:flex;align-items:center;justify-content:center}

  .foot-bg{left:0;top:3880px;width:1200px;height:519px}
  .foot-brand{font-size:32px;color:var(--blue);letter-spacing:.5px}
  .social{width:44px;height:44px;border-radius:50%;background:#fff;box-shadow:0 4px 12px rgba(0,0,0,.1)}
  .social.active{background:var(--blue)}
  .copyright{font-size:14px;color:#222}
</style>
</head>
<body>

<svg class="hero-bg" viewBox="0 0 1200 680" aria-hidden="true">
  <path d="M0 0H1200V529C1110 620 1010 668 900 648C700 610 460 430 256 447C150 456 60 500 0 540Z" fill="var(--sky)"/>
</svg>

<header>
  <div class="abs brand"><span class="dot"></span>Ledgerly</div>
  <nav class="abs nav">
    <a style="left:0">Home</a>
    <a style="left:82px">Services</a>
    <a style="left:178px">About Us</a>
    <a style="left:279px">Contact</a>
    <a class="login" style="left:372px">Login</a>
  </nav>
  <div class="abs lang">EN
    <svg width="7" height="5" viewBox="0 0 7 5"><path d="M1 1l2.5 2.5L6 1" stroke="currentColor" fill="none" stroke-width="1.3"/></svg>
  </div>
</header>

<h1 class="abs hero-title">WELCOME TO<br>LEDGERLY</h1>
<p class="abs hero-text">Lorem ipsum dolor sit amet, consectetur adipiscing elit, sed do eiusmod tempor incididunt ut labore et dolore magna aliqua. Quis ipsum suspendisse ultrices gravida.</p>
<a class="abs btn" style="left:112px;top:405px;width:115px;height:36px">Get Started</a>
<div class="abs hero-art art" role="img" aria-label="Isometric illustration of a server rack connected to laptops, monitors and phones"></div>

<div class="abs art" style="left:145px;top:700px;width:375px;height:333px;background:linear-gradient(140deg,#e9f0fc,#5d86dc 70%,#1f47a8)" role="img" aria-label="Isometric illustration of people working around a laptop and database stacks"></div>
<h2 class="abs section-title" style="left:587px;top:704px">What is it</h2>
<p class="abs copy" style="left:587px;top:762px;width:482px">Ledgerly is a GDPR compliant Membership, Contact Management &amp; List Management solution Ideal replacement for any organisation or company still using spreadsheets, email clients, simple database or pper-based system to manage contact data, mail lists and other personalised information. Ledgerly offers a fast, secure, GDPR compliant solution for managing and coordinating all your Membership and Contact data, and generating GDPR compliant Marketing lists.</p>
<a class="abs btn" style="left:587px;top:987px;width:151px;height:34px">Learn More <span>&rarr;</span></a>

<h2 class="abs section-title" style="left:109px;top:1147px">Standard functionality</h2>
<ul class="abs feature-list" style="left:112px;top:1206px">
  <li>Attendance registration &amp; management</li>
  <li>Time recording</li>
  <li>Relationship management</li>
  <li>Tasks/To-Do's</li>
  <li>Notes/history</li>
  <li>Document storage</li>
  <li>Donation Management</li>
  <li>Prospect Management</li>
</ul>
<a class="abs btn" style="left:111px;top:1466px;width:150px;height:36px">Learn More <span>&rarr;</span></a>
<div class="abs art" style="left:623px;top:1186px;width:393px;height:265px;background:linear-gradient(140deg,#dfe6f7,#8ea6e0 55%,#1e2f78)" role="img" aria-label="Illustration of a businessman working on a laptop beside a plant and a pie chart"></div>

<div class="abs art" style="left:154px;top:1627px;width:396px;height:310px;background:linear-gradient(160deg,#f1f4fc,#c9d7f4 70%,#8aa7e6)" role="img" aria-label="Illustration of a person looking at a large analytics dashboard"></div>
<h2 class="abs section-title" style="left:632px;top:1570px">Full-Service Provision</h2>
<ul class="abs feature-list" style="left:635px;top:1630px">
  <li>Consultancy</li>
  <li>Data Preparation</li>
  <li>De-duplication of existing data (Sheetwise/Mailpost, databases etc.)</li>
  <li>Importation of data - compliant with GDPR requirements</li>
  <li>Installation, configuration and set-up of main system</li>
  <li>Full training</li>
  <li>Technical support</li>
  <li>Optional Customised-Development work</li>
</ul>
<a class="abs btn" style="left:632px;top:1878px;width:151px;height:35px">Learn More <span>&rarr;</span></a>

<div class="abs band"></div>
<article class="abs card" style="left:167px;top:2137px;width:413px;height:376px;padding:40px 38px 0">
  <h3>Challenges most organisa-tions encounter</h3>
  <p style="margin-top:6px">One of the biggest challenges faced when moving from a manual record keeping system (spreadsheets, email, simple database, or paper etc.) is how to manage, and coordinate all the various silos of information, to arrive at a single, valid ‘source of truth’.</p>
  <a class="more" style="display:block;margin-top:17px">Learn More</a>
</article>
<article class="abs card" style="left:649px;top:2137px;width:411px;height:376px;padding:38px 40px 0">
  <h3>Where is the data stored:</h3>
  <p style="margin-top:10px">We provide a fully hosted service within an ISO certified European Data Centre. This can be accessed 24 hours a day, from anywhere you have internet access. Our service provides all the necessary technologies, Hostora Server, Querybase Server and SSL certificates etc., to ensure you can start using the system without requiring additional technical support</p>
  <a class="more" style="display:block;margin-top:11px">Learn More</a>
</article>

<h2 class="abs section-title centered" style="top:2628px">Client Testimonials</h2>
<p class="abs centered" style="top:2685px;font-size:14px;color:#222">This is what our clients said to our questions about Ledgerly.</p>

<svg class="abs" style="left:114px;top:2782px" width="432" height="367" viewBox="0 0 432 367" aria-hidden="true">
  <defs><linearGradient id="blobFill" x1="0" y1="0" x2="0" y2="1">
    <stop offset="0" stop-color="#0a53d6"/><stop offset="1" stop-color="#a9c8f5"/></linearGradient></defs>
  <path d="M250 8C330 -10 420 30 430 110C440 190 380 250 330 300C280 350 190 372 110 360C30 348 -8 300 2 240C12 170 70 130 120 80C165 35 200 18 250 8Z" fill="url(#blobFill)"/>
</svg>
<div class="abs" style="left:405px;top:2862px;width:157px;height:157px;border-radius:50%;background:linear-gradient(160deg,#e7e9ec,#b9bec6);border:4px solid #fff" role="img" aria-label="Portrait photo of a client"></div>

<span class="q-ico" style="left:585px;top:2795px">?</span>
<p class="abs q" style="left:609px;top:2787px;width:445px"><span class="num">Question 1:</span> What is the main benefit/output of the program for you? (Which functions make your work easier and why?)</p>
<span class="chev down" style="left:1071px;top:2802px"></span>
<ul class="abs answers" style="left:621px;top:2885px;width:468px">
  <li>Attendance list tablet - simple overview of present children</li>
  <li>Note function - easy and fast recording of important notes about the child, as well as practical search function. I love the ability to notify other staff about notes - allows for transparent, quick and easy sharing of important information.</li>
</ul>

<div class="abs qcard" style="left:577px;top:3030px;width:531px;height:114px"></div>
<span class="q-ico" style="left:585px;top:3051px">?</span>
<p class="abs q" style="left:609px;top:3043px;width:460px"><span class="num">Question 2:</span> What would it mean to you if you no longer had Ledgerly tomorrow? (Which functions would you miss and why?)</p>
<span class="chev up" style="left:1081px;top:3068px"></span>

<div class="abs qcard" style="left:577px;top:3167px;width:531px;height:85px"></div>
<span class="q-ico" style="left:585px;top:3188px">?</span>
<p class="abs q" style="left:609px;top:3180px;width:460px"><span class="num">Question 3:</span> Are there any other functions you would like to have? (What would these be and why?)</p>
<span class="chev up" style="left:1081px;top:3206px"></span>

<h2 class="abs section-title centered" style="top:3352px">Try Ledgerly</h2>
<p class="abs" style="left:205px;top:3415px;width:790px;text-align:center;font-size:14px;line-height:25.5px;color:#222">Click here to explore Ledgerly yourself. This link provides Read Only access to a test system. This access should provide an insight into how you could manage your club contact data in an efficient, productive, and GDPR compliant manner. Cookie-Statement here.</p>

<div class="abs c-ico" style="left:123px;top:3548px">
  <svg width="18" height="22" viewBox="0 0 18 22"><path d="M9 1a7 7 0 0 0-7 7c0 5 7 13 7 13s7-8 7-13a7 7 0 0 0-7-7z" fill="var(--blue)"/><circle cx="9" cy="8" r="2.6" fill="#fff"/></svg>
</div>
<div class="abs c-title" style="left:188px;top:3546px">Location</div>
<div class="abs c-text" style="left:188px;top:3576px;width:240px">112/bLedgerly. sit amet, consectetur adipiscing</div>

<div class="abs c-ico" style="left:123px;top:3659px">
  <svg width="18" height="18" viewBox="0 0 24 24"><path d="M6.6 10.8a15 15 0 0 0 6.6 6.6l2.2-2.2a1 1 0 0 1 1-.25 11.4 11.4 0 0 0 3.6.57 1 1 0 0 1 1 1V20a1 1 0 0 1-1 1A17 17 0 0 1 3 4a1 1 0 0 1 1-1h3.5a1 1 0 0 1 1 1c0 1.25.2 2.45.57 3.570a1 1 0 0 1-.25 1z" fill="var(--blue)"/></svg>
</div>
<div class="abs c-title" style="left:188px;top:3657px">Phone</div>
<div class="abs c-text" style="left:188px;top:3687px">+1 888 888 8888</div>

<div class="abs c-ico" style="left:123px;top:3748px">
  <svg width="18" height="14" viewBox="0 0 18 14"><rect x="0" y="0" width="18" height="14" rx="2" fill="var(--blue)"/><path d="M1 2l8 6 8-6" stroke="#fff" stroke-width="1.6" fill="none"/></svg>
</div>
<div class="abs c-title" style="left:188px;top:3745px">Email</div>
<div class="abs c-text" style="left:188px;top:3776px">info@ledgerly.example</div>

<form>
  <div class="abs field" style="left:447px;top:3547px;width:316px;height:51px">Name</div>
  <div class="abs field" style="left:447px;top:3615px;width:316px;height:52px">Phone</div>
  <div class="abs field" style="left:447px;top:3682px;width:316px;height:51px">Email</div>
  <div class="abs submit" style="left:446px;top:3750px;width:317px;height:53px">Submit</div>
  <div class="abs field" style="left:784px;top:3547px;width:317px;height:256px">Type your message</div>
</form>

<svg class="abs foot-bg" viewBox="0 0 1200 519" aria-hidden="true">
  <path d="M0 123C180 70 330 20 520 30C760 42 950 40 1200 0V519H0Z" fill="var(--foot)"/>
</svg>
<div class="abs centered" style="top:4146px"><span class="foot-brand">ledgerly</span></div>
<div class="abs social active" style="left:493px;top:4242px"></div>
<div class="abs social" style="left:545px;top:4242px"></div>
<div class="abs social" style="left:596px;top:4242px"></div>
<div class="abs social" style="left:647px;top:4242px"></div>
<p class="abs copyright centered" style="top:4307px">©Copyrights 2023 Company Name &nbsp;&nbsp;|&nbsp;&nbsp; All Rights Reserved</p>

</body>
</html>
```